User Interface design for the Leaf Nanny watering device

Hi Designers

I am designing a new pot plant watering device that clips onto the side of a pot plant and squirts water onto the plant when dry.
I need a designer to come up with an easy to use interface.

Objectives: Simple to understand interface for the average user. User should be able to understand the interface without having to read a manual. The 'feel' should be warm and friendly but also clean. The plan is to print this design on top of any buttons or lights which built into the device. (I can create/move/organise buttons and LED lights, so don't let that constrain the design)

The user interface should have the following options that the user can select:

A. Sensor selection:
1. Semi-wet soil
2. Semi-Dry Soil
3. Wet Soil.
4. Maintain current moisture level

B. Manual override:
1. Water for 5 seconds (small),
2. Water for 10 seconds (medium)
3. Water for 20 seconds (large)
AND
1. Watering frequency 1 day,
2. Watering Frequency 3 days.
3. Watering frequency 7 days.

C. Start/Stop button

Looking forward to your interpretations and designs!
ps: I've already had two logos designed which are provided below and should be incorporated.

Target Market(s)

Home user. Simple to use. Smart home device.

Requirements
Must have
• It should incorporate one of the previous logo designs.

```html
<!DOCTYPE html>
<html lang="en">
<head>
<meta charset="utf-8">
<title>Leaf Nanny – Control Panel</title>
<link rel="stylesheet" href="https://fonts.googleapis.com/css2?family=Open+Sans:wght@400;600;700&display=swap">
<style>
  :root {
    --ink: #111111;
    --paper: #ffffff;
    --rule: #333333;
  }
  html, body {
    margin: 0;
    padding: 0;
    width: 1200px;
    height: 900px;
    overflow: hidden;
    background: var(--paper);
  }
  .panel {
    display: block;
    width: 1200px;
    height: 900px;
    font-family: "Open Sans", Arial, sans-serif;
  }
  .brand-name { font-size: 52px; font-weight: 700; fill: var(--ink); letter-spacing: -1px; }
  .section-rule { stroke: var(--ink); stroke-width: 2; fill: none; }
  .section-tag-box { fill: var(--paper); stroke: var(--ink); stroke-width: 2; }
  .section-tag { font-size: 19px; font-weight: 400; fill: var(--ink); }
  .mode-label { font-size: 10.5px; font-weight: 700; fill: var(--ink); }
  .row-label { font-size: 18px; font-weight: 400; fill: var(--ink); }
  .icon-line { stroke: var(--ink); stroke-width: 3; fill: none; }
  .icon-fill { fill: var(--ink); }
  .amount-ring { fill: var(--paper); stroke: var(--ink); stroke-width: 3; }
  .amount-value { font-size: 24px; font-weight: 400; fill: var(--ink); }
  .key-box { fill: var(--paper); stroke: var(--ink); stroke-width: 3; }
  .key-number { font-size: 22px; font-weight: 400; fill: var(--ink); }
  .key-unit { font-size: 10px; font-weight: 700; fill: var(--ink); }
  .divider { stroke: var(--rule); stroke-width: 2; }
  .power-label { font-size: 20px; font-weight: 400; fill: var(--ink); }
</style>
</head>
<body>
<svg class="panel" viewBox="0 0 1200 900" xmlns="http://www.w3.org/2000/svg">
  <defs>
    <path id="drop" d="M0,-14 C4,-7 10,-1 10,6 A10,10 0 0 1 -10,6 C-10,-1 -4,-7 0,-14 Z"/>
  </defs>

  <!-- Brand -->
  <text class="brand-name" x="600" y="232" text-anchor="middle">Leaf Nanny</text>

  <!-- Soil sensor group -->
  <g class="soil-sensor">
    <path class="section-rule" d="M400,303 V285 H812 V303"/>
    <rect class="section-tag-box" x="545" y="273" width="121" height="25" rx="4"/>
    <text class="section-tag" x="605.5" y="292" text-anchor="middle">Soil Sensor</text>

    <!-- Semi-dry -->
    <g class="mode mode-semi-dry" transform="translate(396,342)">
      <circle class="icon-line" r="12"/>
      <path class="icon-fill" d="M0,-12 A12,12 0 0 1 0,12 Z"/>
      <g class="icon-line" stroke-width="2.5">
        <line x1="0" y1="-16" x2="0" y2="-23"/>
        <line x1="0" y1="16" x2="0" y2="23"/>
        <line x1="-16" y1="0" x2="-23" y2="0"/>
        <line x1="16" y1="0" x2="23" y2="0"/>
        <line x1="-12" y1="-12" x2="-17" y2="-17"/>
        <line x1="12" y1="-12" x2="17" y2="-17"/>
        <line x1="-12" y1="12" x2="-17" y2="17"/>
        <line x1="12" y1="12" x2="17" y2="17"/>
      </g>
    </g>
    <text class="mode-label" x="394" y="394" text-anchor="middle">SEMI-DRY</text>

    <!-- Semi-wet -->
    <g class="mode mode-semi-wet" transform="translate(536,340) scale(1.15)">
      <use href="#drop" class="icon-line" stroke-width="2.5"/>
      <path class="icon-fill" d="M0,-14 C4,-7 10,-1 10,6 A10,10 0 0 1 0,16 Z"/>
    </g>
    <text class="mode-label" x="536" y="394" text-anchor="middle">SEMI-WET</text>

    <!-- Wet -->
    <g class="mode mode-wet" transform="translate(687,340) scale(1.2)">
      <use href="#drop" class="icon-fill"/>
    </g>
    <text class="mode-label" x="689" y="394" text-anchor="middle">WET</text>

    <!-- Maintain moisture -->
    <g class="mode mode-maintain" transform="translate(810,344)">
      <path class="icon-line" d="M9,-22 A24,24 0 1 0 20,-12"/>
      <path class="icon-fill" d="M6,-30 L17,-22 L5,-15 Z"/>
      <g transform="translate(0,1) scale(0.85)"><use href="#drop" class="icon-fill"/></g>
    </g>
    <text class="mode-label" x="808" y="394" text-anchor="middle">MAINTAIN</text>
    <text class="mode-label" x="808" y="406" text-anchor="middle">MOISTURE</text>
  </g>

  <!-- Watering group -->
  <g class="watering">
    <path class="section-rule" d="M400,486 V459 H812 V486"/>
    <rect class="section-tag-box" x="543" y="446" width="125" height="26" rx="4"/>
    <text class="section-tag" x="605.5" y="466" text-anchor="middle">Watering</text>

    <!-- Amount -->
    <text class="row-label" x="373" y="528">Amount</text>

    <g class="amount amount-small">
      <g transform="translate(476,522) scale(0.5)"><use href="#drop" class="icon-fill"/></g>
      <g transform="translate(488,522) scale(0.5)"><use href="#drop" class="icon-fill"/></g>
      <circle class="amount-ring" cx="523" cy="520" r="25"/>
      <text class="amount-value" x="523" y="529" text-anchor="middle">5s</text>
    </g>

    <g class="amount amount-medium">
      <g transform="translate(612,512) scale(0.5)"><use href="#drop" class="icon-fill"/></g>
      <g transform="translate(624,512) scale(0.5)"><use href="#drop" class="icon-fill"/></g>
      <g transform="translate(612,528) scale(0.5)"><use href="#drop" class="icon-fill"/></g>
      <g transform="translate(624,528) scale(0.5)"><use href="#drop" class="icon-fill"/></g>
      <circle class="amount-ring" cx="658" cy="520" r="25"/>
      <text class="amount-value" x="658" y="529" text-anchor="middle">10s</text>
    </g>

    <g class="amount amount-large">
      <g transform="translate(731,512) scale(0.5)"><use href="#drop" class="icon-fill"/></g>
      <g transform="translate(743,512) scale(0.5)"><use href="#drop" class="icon-fill"/></g>
      <g transform="translate(755,512) scale(0.5)"><use href="#drop" class="icon-fill"/></g>
      <g transform="translate(767,512) scale(0.5)"><use href="#drop" class="icon-fill"/></g>
      <g transform="translate(731,528) scale(0.5)"><use href="#drop" class="icon-fill"/></g>
      <g transform="translate(743,528) scale(0.5)"><use href="#drop" class="icon-fill"/></g>
      <g transform="translate(755,528) scale(0.5)"><use href="#drop" class="icon-fill"/></g>
      <g transform="translate(767,528) scale(0.5)"><use href="#drop" class="icon-fill"/></g>
      <circle class="amount-ring" cx="800" cy="520" r="25"/>
      <text class="amount-value" x="800" y="529" text-anchor="middle">20s</text>
    </g>

    <!-- Frequency -->
    <text class="row-label" x="367" y="633">Frequency</text>

    <g class="frequency freq-1">
      <rect class="key-box" x="497" y="604" width="58" height="48" rx="8"/>
      <text class="key-number" x="526" y="630" text-anchor="middle">1</text>
      <text class="key-unit" x="526" y="645" text-anchor="middle">DAY</text>
    </g>
    <g class="frequency freq-3">
      <rect class="key-box" x="631" y="604" width="58" height="48" rx="8"/>
      <text class="key-number" x="660" y="630" text-anchor="middle">3</text>
      <text class="key-unit" x="660" y="645" text-anchor="middle">DAYS</text>
    </g>
    <g class="frequency freq-7">
      <rect class="key-box" x="771" y="604" width="58" height="48" rx="8"/>
      <text class="key-number" x="800" y="630" text-anchor="middle">7</text>
      <text class="key-unit" x="800" y="645" text-anchor="middle">DAYS</text>
    </g>
  </g>

  <line class="divider" x1="363" y1="681" x2="845" y2="681"/>

  <!-- Start / stop -->
  <g class="power">
    <rect class="key-box" x="569" y="705" width="57" height="48" rx="8"/>
    <path class="icon-line" stroke-width="2.5" d="M589,720 A14,14 0 1 0 606,720"/>
    <line class="icon-line" stroke-width="2.5" x1="597.5" y1="714" x2="597.5" y2="729"/>
    <text class="power-label" x="639" y="738">START/STOP</text>
  </g>
</svg>
</body>
</html>
```